Geschäftspapiere für medizinische Schutzausrüstung
Zielgruppe
Medizinische Schutzausrüstung für Deutschland.
Zertifiziert, schnell und unkompliziert.
Für Einrichtungen im Bereich Medizin & Pflege, systemrelevante Industrien sowie für öffentliche Träger.
Aufgabenstellung
Es sollte clean sein, Farben wie , Weiß, blau, grün, wären von Vorteil. Habe keine besondere Vorstellungen lasse mich gerne überraschen.
Siehe .. www.tovrk.de

```html
<!DOCTYPE html>
<html lang="de">
<head>
<meta charset="utf-8">
<title>TOVRK – Briefbogen</title>
<link rel="stylesheet" href="https://fonts.googleapis.com/css2?family=Lato:wght@300;400;700&display=swap">
<style>
  :root {
    --mint: #8ecbb0;
    --mint-light: #b9dcb8;
    --sun: #f3e57a;
    --navy: #1c2740;
    --cyan: #1ba1d6;
    --teal: #2c9fb5;
    --grey: #6b6b6b;
    --rule: #bdbdbd;
    --paper: #ffffff;
    --ghost: #f1f3f4;
  }
  * { margin: 0; padding: 0; box-sizing: border-box; }
  html, body { width: 866px; height: 1200px; overflow: hidden; background: var(--paper); }
  body { font-family: "Lato", sans-serif; color: var(--navy); }
  .letterhead { position: relative; width: 866px; height: 1200px; background: var(--paper); overflow: hidden; }

  .band-top { position: absolute; left: 0; top: 0; width: 484px; height: 21px; }
  .band-bottom { position: absolute; left: 0; top: 1169px; width: 866px; height: 31px; }

  .brand { position: absolute; left: 656px; top: 37px; width: 161px; text-align: center; }
  .brand-dot { display: block; width: 84px; height: 84px; margin: 0 auto 20px; border-radius: 50%; background: var(--teal); }
  .brand-name { display: block; font-weight: 300; font-size: 40px; letter-spacing: 8px; line-height: 1; margin-right: -8px; color: var(--navy); white-space: nowrap; }
  .brand-rule { display: block; height: 3px; background: var(--cyan); margin-top: 9px; }

  .return-address { position: absolute; left: 91px; top: 238px; font-size: 10.5px; color: var(--grey); border-bottom: 1px solid var(--rule); padding-bottom: 1px; }
  .return-address .sep { color: var(--sun); }

  .contact { position: absolute; left: 692px; top: 262px; height: 108px; border-left: 1px solid var(--navy); padding-left: 16px; font-style: normal; }
  .contact-address { font-size: 12.5px; font-weight: 700; line-height: 13px; margin-top: -4px; }
  .contact-list { list-style: none; margin-top: 20px; }
  .contact-list li { display: flex; align-items: center; height: 19px; font-size: 10px; font-weight: 700; white-space: nowrap; }
  .contact-list svg { width: 12px; height: 12px; margin-right: 10px; flex: none; }

  .fold-mark { position: absolute; left: 0; width: 31px; height: 1px; background: var(--cyan); }
  .fold-mark.upper { top: 421px; }
  .fold-mark.lower { top: 824px; }

  .watermark { position: absolute; left: 0; top: 560px; width: 866px; text-align: center; font-weight: 300; font-size: 90px; letter-spacing: 16px; color: var(--ghost); white-space: nowrap; }

  .legal { position: absolute; top: 1170px; left: 0; width: 866px; height: 30px; font-size: 10.5px; font-weight: 400; color: var(--paper); line-height: 14px; }
  .legal span { position: absolute; white-space: nowrap; }
  .legal .r1 { top: 1px; }
  .legal .r2 { top: 15px; }
  .legal .divider { position: absolute; top: 3px; width: 1px; height: 23px; background: var(--paper); }
</style>
</head>
<body>
<main class="letterhead">

  <svg class="band-top" viewBox="0 0 484 21" role="img" aria-label="Dekoratives Streifenband in Mint und Gelb">
    <defs>
      <linearGradient id="bandTopFill" x1="0" x2="1" y1="0" y2="0">
        <stop offset="0" stop-color="var(--mint)"/>
        <stop offset="0.25" stop-color="var(--mint-light)"/>
        <stop offset="0.45" stop-color="var(--mint)"/>
      </linearGradient>
    </defs>
    <polygon points="0,0 484,0 464,21 0,21" fill="url(#bandTopFill)"/>
  </svg>

  <header class="brand">
    <span class="brand-dot"></span>
    <span class="brand-name">TOVRK</span>
    <span class="brand-rule"></span>
  </header>

  <p class="return-address">Lindenhofweg 12 <span class="sep">|</span> 30421 Wesselbach</p>

  <address class="contact">
    <p class="contact-address">Marktgasse 17<br>31187 Auenfeld</p>
    <ul class="contact-list">
      <li>
        <svg viewBox="0 0 12 12" fill="var(--sun)"><path d="M2.5 0.8l2 2.2-1.2 1.4c.7 1.6 1.9 2.8 3.4 3.5l1.4-1.2 2.2 2-1.2 2.3C5.2 10.5 1.5 6.8.5 1.9z"/></svg>
        040 / 58203917
      </li>
      <li>
        <svg viewBox="0 0 12 12" fill="none" stroke="var(--sun)" stroke-width="1.2"><rect x="1" y="4.5" width="10" height="5.5" rx="1"/><path d="M3 4.5V1.5h6v3M3 10v-2h6v2"/></svg>
        040 / 58203917
      </li>
      <li>
        <svg viewBox="0 0 12 12" fill="none" stroke="var(--sun)" stroke-width="1.1"><circle cx="6" cy="6" r="5"/><ellipse cx="6" cy="6" rx="2.2" ry="5"/><path d="M1 6h10M2 3.3h8M2 8.7h8"/></svg>
        www.tovrk.de
      </li>
      <li>
        <svg viewBox="0 0 12 12" fill="none" stroke="var(--sun)" stroke-width="1.2"><path d="M1 5l5-3.5L11 5v5.5H1z"/><path d="M1 5l5 3.5L11 5"/></svg>
        anfrage@tovrk.de
      </li>
    </ul>
  </address>

  <span class="fold-mark upper"></span>
  <span class="fold-mark lower"></span>

  <div class="watermark" aria-hidden="true">TOVRK</div>

  <svg class="band-bottom" viewBox="0 0 866 31" role="img" aria-label="Dekoratives Streifenband in Mint und Gelb">
    <defs>
      <linearGradient id="bandBottomFill" x1="0" x2="1" y1="0" y2="0">
        <stop offset="0" stop-color="var(--mint)"/>
        <stop offset="0.1" stop-color="var(--mint-light)"/>
        <stop offset="0.2" stop-color="var(--mint)"/>
      </linearGradient>
    </defs>
    <rect width="866" height="31" fill="url(#bandBottomFill)"/>
  </svg>

  <footer class="legal">
    <span class="r1" style="left:255px">Bank:</span>
    <span class="r1" style="left:287px">Talbank eG</span>
    <span class="r2" style="left:287px">Auenfeld</span>
    <i class="divider" style="left:360px"></i>
    <span class="r1" style="left:369px">USt-IdNr.:</span>
    <span class="r1" style="left:430px">DE418205739</span>
    <span class="r2" style="left:369px">Register-Nr.</span>
    <span class="r2" style="left:430px">HRA 3172</span>
    <i class="divider" style="left:508px"></i>
    <span class="r1" style="left:517px">Amtsgericht</span>
    <span class="r1" style="left:579px">Auenfeld</span>
    <span class="r2" style="left:517px">Sitz</span>
    <span class="r2" style="left:579px">Auenfeld</span>
    <i class="divider" style="left:637px"></i>
    <span class="r1" style="left:645px">BIC</span>
    <span class="r1" style="left:673px">TALBDEF1AUF</span>
    <span class="r2" style="left:645px">IBAN</span>
    <span class="r2" style="left:673px">DE71 2806 4417 5520 3184 00</span>
  </footer>

</main>
</body>
</html>
```